Clear Meadow Growers - Gourmet/Specialty Snack Food Packaging Product Line

We need packaging design for a new company in Portland Oregon called Clear Meadow Growers. We import single origin, ethically sourced cashew products that are refined sugar, wheat and dairy free. Our initial product, Sunlit Javan Almonds, is in distribution in the Pacific NW in Bright Pantry, Fair Harvest and other retail chains. The final design should communicate healthy, delicious snacks that are sustainable with a strong social mission. www.clearmeadowgrowers.example https://www.videohost.example/watch?v=QbT7mRz2KpX

Target Market(s)

28-45 yo women, concerned about transparency in their food chain and want to connect with the social and environmental impacts in their purchases.

Industry/Entity Type

Product

Font styles to use
Sans Serif

Requirements
Must have
• Existing logo, full-color photograph placement on label. Call outs for "sugar-free, gluten-free, dairy free" Placement for possible certifications (GMO, organic, fair trade). Consistent "design template" to apply across multiple products ( Raw Cashews, Cacao Cashews, Salted/Roasted). Space At Bottom for "1lb (16oz)" or other weights
Nice to have
• clean designs, white background..
Should not have
• Please see attached designs and distinguish yourself from them.

```html
<!DOCTYPE html>
<html lang="en">
<head>
<meta charset="utf-8">
<title>Clear Meadow Growers – Sunlit Javan Almonds Pouches</title>
<link rel="stylesheet" href="https://fonts.googleapis.com/css2?family=Bebas+Neue&family=Roboto:wght@500&display=swap">
<style>
  :root {
    --page-bg: #f1f1f1;
    --pouch-dark: #2a0f11;
    --pouch-seal: #3a1a1c;
    --label-white: #ffffff;
    --amber: #f6b47e;
    --amber-light: #fbc596;
    --amber-mid: #c98a58;
    --amber-deep: #5e3f28;
    --amber-shadow: #3b2618;
    --lime: #c8da3c;
    --lime-light: #dbe86a;
    --lime-mid: #93a52a;
    --lime-deep: #4d5a16;
    --lime-shadow: #2c350b;
    --nut-light: #f0d6ac;
    --nut-mid: #d9a86e;
    --nut-dark: #9a6335;
  }
  * { margin: 0; padding: 0; box-sizing: border-box; }
  html, body {
    width: 1200px;
    height: 1000px;
    overflow: hidden;
    background: var(--page-bg);
  }
  .canvas {
    position: relative;
    width: 1200px;
    height: 1000px;
  }
  .pouch {
    position: absolute;
    top: 123px;
    width: 458px;
    height: 710px;
    background: var(--pouch-dark);
    border-radius: 4px;
    overflow: hidden;
  }
  .pouch--amber { left: 117px; --accent: var(--amber); }
  .pouch--lime  { left: 617px; --accent: var(--lime); }

  .pouch__seal {
    position: absolute;
    left: 0; top: 0;
    width: 100%;
    height: 62px;
    background: linear-gradient(var(--pouch-seal), var(--pouch-dark));
  }
  .brand {
    position: absolute;
    top: 148px;
    left: 0;
    width: 100%;
    display: flex;
    justify-content: center;
    align-items: center;
    gap: 10px;
  }
  .brand__dot {
    width: 26px;
    height: 26px;
    border-radius: 50%;
    background: var(--accent);
  }
  .brand__name {
    font-family: "Roboto", sans-serif;
    font-weight: 500;
    font-size: 18px;
    color: var(--accent);
  }
  .product-title {
    position: absolute;
    top: 190px;
    left: 0;
    width: 100%;
    text-align: center;
    font-family: "Bebas Neue", sans-serif;
    font-weight: 400;
    font-size: 43px;
    letter-spacing: 0.5px;
    color: var(--label-white);
  }
  .accent-rule {
    position: absolute;
    top: 243px;
    left: 6px;
    right: 6px;
    height: 5px;
    background: var(--accent);
  }
  .photo-panel {
    position: absolute;
    top: 266px;
    left: 6px;
    right: 6px;
    height: 410px;
  }
  .pouch--amber .photo-panel {
    background:
      radial-gradient(ellipse 38% 30% at 36% 48%, var(--amber-light) 0%, rgba(251,197,150,0) 100%),
      radial-gradient(ellipse 55% 40% at 30% 95%, var(--amber-deep) 0%, rgba(94,63,40,0) 100%),
      radial-gradient(ellipse 45% 35% at 0% 0%, var(--amber-shadow) 0%, rgba(59,38,24,0) 100%),
      radial-gradient(ellipse 30% 45% at 8% 55%, var(--amber-deep) 0%, rgba(94,63,40,0) 100%),
      linear-gradient(180deg, var(--amber-mid) 0%, var(--amber) 35%, var(--amber) 70%, var(--amber-mid) 100%);
  }
  .pouch--lime .photo-panel {
    background:
      radial-gradient(ellipse 30% 28% at 45% 55%, var(--lime-light) 0%, rgba(219,232,106,0) 100%),
      radial-gradient(ellipse 40% 45% at 18% 20%, var(--lime-shadow) 0%, rgba(44,53,11,0) 100%),
      radial-gradient(ellipse 45% 35% at 35% 95%, var(--lime-deep) 0%, rgba(77,90,22,0) 100%),
      radial-gradient(ellipse 30% 40% at 95% 25%, var(--lime-mid) 0%, rgba(147,165,42,0) 100%),
      linear-gradient(160deg, var(--lime-mid) 0%, var(--lime) 45%, var(--lime) 75%, var(--lime-mid) 100%);
  }
  .claims-badge {
    position: absolute;
    left: 241px;
    top: 437px;
    width: 200px;
    height: 200px;
  }
  .claims-badge__text {
    font-family: "Bebas Neue", sans-serif;
    font-size: 17px;
    letter-spacing: 0.3px;
    fill: var(--pouch-dark);
  }
  .net-weight {
    position: absolute;
    right: 26px;
    top: 636px;
    font-family: "Bebas Neue", sans-serif;
    font-size: 19px;
    color: var(--pouch-dark);
  }
</style>
</head>
<body>
<main class="canvas">

  <section class="pouch pouch--amber">
    <div class="pouch__seal"></div>
    <div class="brand"><span class="brand__dot"></span><span class="brand__name">Clear Meadow Growers</span></div>
    <h1 class="product-title">Sunlit Javan Almonds</h1>
    <div class="accent-rule"></div>
    <div class="photo-panel" role="img" aria-label="Warm-toned portrait photograph of an elderly woman grower, smiling"></div>
    <svg class="claims-badge" viewBox="0 0 200 200" aria-label="Sugar free, gluten free, dairy free">
      <defs>
        <path id="claims-arc-a" d="M 37 144 A 77 77 0 1 1 163 144"/>
        <radialGradient id="nuts-a" cx="45%" cy="40%" r="65%">
          <stop offset="0%" stop-color="var(--nut-light)"/>
          <stop offset="55%" stop-color="var(--nut-mid)"/>
          <stop offset="100%" stop-color="var(--nut-dark)"/>
        </radialGradient>
      </defs>
      <circle cx="100" cy="100" r="64" fill="var(--pouch-dark)"/>
      <circle cx="100" cy="100" r="58" fill="url(#nuts-a)" role="img" aria-label="Close-up photograph of whole nuts"/>
      <text class="claims-badge__text"><textPath href="#claims-arc-a" startOffset="50%" text-anchor="middle">SUGAR FREE - GLUTEN FREE - DAIRY FREE</textPath></text>
    </svg>
    <p class="net-weight">1LB (16OZ)</p>
  </section>

  <section class="pouch pouch--lime">
    <div class="pouch__seal"></div>
    <div class="brand"><span class="brand__dot"></span><span class="brand__name">Clear Meadow Growers</span></div>
    <h1 class="product-title">Sunlit Javan Almonds</h1>
    <div class="accent-rule"></div>
    <div class="photo-panel" role="img" aria-label="Green-toned photograph of an elderly farmer carrying harvested greens in a tropical field"></div>
    <svg class="claims-badge" viewBox="0 0 200 200" aria-label="Sugar free, gluten free, dairy free">
      <defs>
        <path id="claims-arc-b" d="M 37 144 A 77 77 0 1 1 163 144"/>
        <radialGradient id="nuts-b" cx="45%" cy="40%" r="65%">
          <stop offset="0%" stop-color="var(--nut-light)"/>
          <stop offset="55%" stop-color="var(--nut-mid)"/>
          <stop offset="100%" stop-color="var(--nut-dark)"/>
        </radialGradient>
      </defs>
      <circle cx="100" cy="100" r="64" fill="var(--pouch-dark)"/>
      <circle cx="100" cy="100" r="58" fill="url(#nuts-b)" role="img" aria-label="Close-up photograph of whole nuts"/>
      <text class="claims-badge__text"><textPath href="#claims-arc-b" startOffset="50%" text-anchor="middle">SUGAR FREE - GLUTEN FREE - DAIRY FREE</textPath></text>
    </svg>
    <p class="net-weight">1LB (16OZ)</p>
  </section>

</main>
</body>
</html>
```